Label Design for 2x Chutney Products

We need a label design for 2x Chutney Products.
Zintara Chutney - Red Chili
Zintara Chutney - Green Chili & Coriander
See attached pictures. This is just sample pictures so you get an impression of the product and the colors. Both labels to have as title the generic name "Zintara Chutney" and then added either Red Chili or Green Chili & Coriander. The different terms needs to be good readable and can differ in font/color/size, or in the same style if this makes more sense from design point (as I am not a designer). The labels later on need to be editable in the way that the ingredient list, nutrition list, basis company and production information can be added. If this needs to be done directly and cannot be edited later on please let know. Editable design related the additional text also would be good as the additional information need to be added in different languages (Dutch. German and perhaps French). No clue how this is to be implemented but looking forward to receive some input/solutions on this.
I already had a project to create the company logo. I consider this logo to be used as the product logo and not the company logo. A different company logo later on can be designed from new. This logo is here attached. Either to work with this logo and use it as product logo (perhaps revise the colors) and add the product description or create a new logo for the product from scratch if you feel too. The logo itself should be easily readable for the product name/description and the colors appealing to such product and of course customers.
Please contact if any clarification needed. Thanks in advance for your efforts and ideas for this project.

Industry/Entity Type

Food

Other font styles liked:
• Asian Touch

Requirements
Nice to have
• If possible "simply" editable for text fields in order to add/revise the ingredient list, nutrition list, revise to different languages.

```html
<!DOCTYPE html>
<html lang="en">
<head>
<meta charset="utf-8">
<title>Zintara Chutney – Labels</title>
<link rel="stylesheet" href="https://fonts.googleapis.com/css2?family=Montserrat:wght@500;700&family=Mystery+Quest&display=swap">
<style>
  :root {
    --page-bg: #e4e4e6;
    --white: #ffffff;
    --ink: #1b1b1b;
    --red-deep: #b3141e;
    --red-light: #ee6464;
    --red-photo-a: #c91a1f;
    --red-photo-b: #8f0e12;
    --red-type: #d9262b;
    --green-deep: #3c7323;
    --green-light: #72b82b;
    --green-photo-a: #4f8f2a;
    --green-photo-b: #2c5a17;
    --green-type: #4e8a25;
  }
  * { box-sizing: border-box; margin: 0; padding: 0; }
  html, body { width: 1200px; height: 759px; overflow: hidden; }
  body {
    background: var(--page-bg);
    font-family: "Montserrat", Arial, sans-serif;
    display: flex;
    flex-direction: column;
    justify-content: center;
    align-items: center;
    gap: 40px;
  }
  .label {
    position: relative;
    width: 1160px;
    height: 298px;
    overflow: hidden;
  }
  .label--red { background: linear-gradient(90deg, var(--red-deep), var(--red-light)); }
  .label--green { background: linear-gradient(90deg, var(--green-deep), var(--green-light)); }
  .label__art { position: absolute; inset: 0; width: 100%; height: 100%; }
  .label__ingredients {
    position: absolute;
    left: 45px;
    top: 46px;
    width: 215px;
    font-size: 8.5px;
    line-height: 1.35;
    font-weight: 500;
    color: var(--white);
  }
  .label__badge {
    position: absolute;
    left: 415px;
    top: 0;
    width: 330px;
    height: 298px;
    display: flex;
    flex-direction: column;
    align-items: center;
    justify-content: center;
    text-align: center;
  }
  .brand {
    display: flex;
    align-items: center;
    gap: 6px;
    font-family: "Montserrat", Arial, sans-serif;
    font-weight: 700;
    font-size: 13px;
    line-height: 1;
    letter-spacing: 0.5px;
    text-transform: uppercase;
    color: var(--ink);
    margin-bottom: 14px;
  }
  .brand__dot {
    width: 14px; height: 14px; border-radius: 50%;
    background: var(--red-type);
  }
  .product-title {
    font-family: "Mystery Quest", cursive;
    font-size: 44px;
    line-height: 1;
    color: var(--ink);
    white-space: nowrap;
  }
  .flavour {
    font-family: "Mystery Quest", cursive;
    font-size: 27px;
    line-height: 1.05;
    margin-top: 10px;
  }
  .flavour--red { color: var(--red-type); }
  .flavour--green { color: var(--green-type); font-size: 24px; }
  .flavour__amp { font-size: 13px; }
</style>
</head>
<body>

  <section class="label label--red">
    <svg class="label__art" viewBox="0 0 1160 298" aria-hidden="false">
      <defs>
        <radialGradient id="redPhoto" cx="50%" cy="50%" r="60%">
          <stop offset="0%" stop-color="var(--red-photo-a)"/>
          <stop offset="100%" stop-color="var(--red-photo-b)"/>
        </radialGradient>
      </defs>
      <ellipse cx="585" cy="150" rx="290" ry="230" fill="url(#redPhoto)" role="img" aria-label="Photograph of fresh red chili peppers surrounding the badge"/>
      <circle cx="580" cy="150" r="165" fill="var(--white)"/>
    </svg>
    <p class="label__ingredients">Ingredients: Lorem ipsum dolor sit amet, consectetur adipiscing elit, sed do eiusmod tempor incididunt ut labore et dolore magna aliqua. Et sollicitudin ac orci phasellus egestas.</p>
    <div class="label__badge">
      <div class="brand"><span class="brand__dot"></span>Orvelo Foods</div>
      <h1 class="product-title">Zintara Chutney</h1>
      <p class="flavour flavour--red">Red Chili</p>
    </div>
  </section>

  <section class="label label--green">
    <svg class="label__art" viewBox="0 0 1160 298">
      <defs>
        <radialGradient id="greenPhoto" cx="50%" cy="50%" r="60%">
          <stop offset="0%" stop-color="var(--green-photo-a)"/>
          <stop offset="100%" stop-color="var(--green-photo-b)"/>
        </radialGradient>
      </defs>
      <ellipse cx="585" cy="150" rx="290" ry="230" fill="url(#greenPhoto)" role="img" aria-label="Photograph of green chili peppers and fresh coriander leaves surrounding the badge"/>
      <circle cx="580" cy="150" r="165" fill="var(--white)"/>
    </svg>
    <p class="label__ingredients">Ingredients: Lorem ipsum dolor sit amet, consectetur adipiscing elit, sed do eiusmod tempor incididunt ut labore et dolore magna aliqua. Et sollicitudin ac orci phasellus egestas.</p>
    <div class="label__badge">
      <div class="brand"><span class="brand__dot"></span>Orvelo Foods</div>
      <h1 class="product-title">Zintara Chutney</h1>
      <p class="flavour flavour--green">Green Chili<br><span class="flavour__amp">&amp;</span> Coriander</p>
    </div>
  </section>

</body>
</html>
```